Wandering Past Chronicles - Book Cover Design

I need a cover (front, spine, back) designed for the second edition of the historical book - Wandering Past Chronicles. This book was created to be a more engaging supplementary resource to the dry texts of most middle and high school social studies classrooms. Although comprehensive and exhaustively researched, the book at times uses humor and irony to engage the reader. The cover should reflect this tone.

Book Title: Wandering Past Chronicles
Subtitle: The Legends, Customs and Crossroads of Human Memory and the Local Dilemmas of Our Age
Author: Tobias Holloway
Updates

Project Deadline Extended
Reason: As multiple designers are working on adjustments and I am looking for new, creative ideas, I am extending the deadline five days. Thank you.

Project Deadline Extended
Reason: Artists are still making alterations to suggestions made and I also want to give designers a chance to submit new ideas.

Target Market(s)

Middle School and High School Teachers

Font styles to use
Serif

Colors
ec1f27
ffffff
000000

Requirements
Must have
• 1) See attachment for text for front cover, spine, back cover
• 2) Central, engaging image
Nice to have
• A subtle hint of humor, light tone
• Potentially upside down globe spinning
• Prefer black, red, white color scheme
Should not have
• Cartoonish text, images

```html
<!DOCTYPE html>
<html lang="en">
<head>
<meta charset="utf-8">
<title>Wandering Past Chronicles — Cover Wrap</title>
<link href="https://fonts.googleapis.com/css2?family=Crimson+Text:wght@400;600&family=Open+Sans:wght@600;700;800&display=swap" rel="stylesheet">
<style>
  :root {
    --red: #ec1f27;
    --white: #ffffff;
    --paper: #f4f3f0;
    --black: #000000;
    --ink: #2b2b2b;
    --ink-soft: #3a3a3a;
    --stage: #ececec;
    --serif: "Crimson Text", Georgia, serif;
    --sans: "Open Sans", Arial, sans-serif;
  }
  * { box-sizing: border-box; margin: 0; padding: 0; }
  html, body { width: 1200px; height: 1200px; overflow: hidden; }
  body { background: var(--stage); position: relative; }

  .cover-wrap {
    position: absolute; left: 70px; top: 220px;
    width: 1060px; height: 760px;
    display: flex;
    box-shadow: 0 10px 30px rgba(0,0,0,.18);
  }

  /* ---------- back cover ---------- */
  .back-cover {
    position: relative; width: 500px; height: 100%;
    background: var(--ink); overflow: hidden; color: var(--white);
  }
  .back-cover .shapes { position: absolute; inset: 0; }
  .back-copy {
    position: relative; padding: 44px 46px 0;
    font-family: var(--sans);
  }
  .back-headline {
    font-weight: 800; font-size: 22px; text-align: center; margin-bottom: 12px;
  }
  .back-body p {
    font-weight: 600; font-size: 12px; line-height: 1.4;
    text-align: justify; margin-bottom: 7px;
  }
  .back-rule { border: 0; border-top: 1px solid var(--white); margin: 10px 0 9px; }
  .back-quote {
    font-weight: 700; font-size: 12px; line-height: 1.4; text-align: center;
    padding: 0 10px;
  }
  .barcode-space {
    position: absolute; right: 46px; bottom: 26px;
    width: 180px; height: 96px; background: var(--white);
  }

  /* ---------- spine ---------- */
  .spine {
    width: 60px; height: 100%; background: var(--ink);
    position: relative;
  }
  .spine-title, .spine-author {
    position: absolute; left: 50%; white-space: nowrap;
    font-family: var(--serif);
  }
  .spine-title {
    top: 300px; color: var(--white); font-size: 25px; letter-spacing: 2px;
    transform: translate(-50%, -50%) rotate(90deg);
  }
  .spine-author {
    top: 680px; color: var(--red); font-size: 13px; letter-spacing: 1.5px;
    font-variant: small-caps;
    transform: translate(-50%, -50%) rotate(90deg);
  }

  /* ---------- front cover ---------- */
  .front-cover {
    position: relative; width: 500px; height: 100%;
    background: var(--paper); overflow: hidden;
  }
  .front-cover .shapes { position: absolute; inset: 0; }
  .edition {
    position: absolute; top: 62px; left: 232px;
    font-family: var(--serif); color: var(--white); font-size: 22px;
  }
  .title {
    position: absolute; top: 104px; left: 40px; right: 20px;
    font-family: var(--serif); font-weight: 600; color: var(--red);
    font-size: 72px; line-height: .9; text-transform: uppercase;
    letter-spacing: -1px;
  }
  .title span { display: block; }
  .title .line-2 { padding-left: 90px; }
  .globe {
    position: absolute; top: 378px; left: 128px;
    width: 236px; height: 236px; border-radius: 50%;
    background: radial-gradient(circle at 38% 35%, #6a6a6a, #2e2e2e 60%, #1b1b1b);
  }
  .globe-shadow {
    position: absolute; top: 628px; left: 150px; width: 190px; height: 10px;
    border-radius: 50%;
    background: radial-gradient(ellipse, rgba(0,0,0,.35), transparent 70%);
  }
  .subtitle {
    position: absolute; top: 648px; left: 40px; right: 40px;
    font-family: var(--serif); color: var(--black); text-align: center;
    font-size: 17px; line-height: 1.2;
  }
  .author {
    position: absolute; bottom: 22px; left: 0; right: 0; text-align: center;
    font-family: var(--serif); color: var(--red); font-size: 30px;
    font-variant: small-caps; letter-spacing: .5px;
  }
</style>
</head>
<body>
<main class="cover-wrap">

  <section class="back-cover">
    <svg class="shapes" viewBox="0 0 500 760" preserveAspectRatio="none" aria-hidden="true">
      <path d="M0 540 C40 600 30 660 70 700 C110 740 130 760 170 760 L0 760 Z" fill="#f4f3f0"/>
      <path d="M430 760 C440 720 470 700 500 690 L500 760 Z" fill="#f4f3f0"/>
      <path d="M120 90 C170 60 260 70 330 110 C380 140 360 200 300 220 C230 240 140 210 110 170 C90 140 95 105 120 90 Z" fill="#3a3a3a"/>
      <path d="M60 560 C120 520 220 540 260 600 C290 650 240 700 170 690 C100 680 40 620 60 560 Z" fill="#3a3a3a"/>
    </svg>
    <div class="back-copy">
      <h2 class="back-headline">Do you know how we got to here?</h2>
      <div class="back-body">
        <p>Well, if you’re like 97.4% of the people walking the planet, you haven’t got a clue. Sure, you might know a bit about a couple rivers in Mesopotamia, how Philo Andrakis wandered around Athens asking questions or how Brother Anselm Kroll got ticked off one day and nailed a really long essay to the door of a church. But to be honest (and don’t be embarrassed), you’ve got some gaps.</p>
        <p>Be dense no more. In Wandering Past Chronicles, Tobias Holloway once again takes you through all the major tales, traditions and turning points of world history - not just European history, but WORLD history. You’ll figure out real quick that the West might have had some crowning moments, but for the whole of human history, it’s been the Persians, the Indians, the Chinese, the Muslims or some horse peoples from the steppe that have truly turned us into the clever little creatures we are today. And while most world history books fade off once the Cold War comes to a close, this sometimes sardonic tome just gets going. Updated to include contemporary debates over topics such as the Channel Split, the rise of the Crescent Front, claims to the South China Sea, the mounting refugee crisis and the controversial presidency of Harlan Vance, this second edition finishes with a distinctively comprehensive look at the 21st century challenges facing nine major regions of today’s world - Africa, Latin America, Japan, China, the Middle East, India, Russia, Europe and the United States.</p>
      </div>
      <hr class="back-rule">
      <p class="back-quote">“ Tobias Holloway expertly understands what his audience wants to know, what they need to know. A page-turning account of our proudest achievements and our most colossal bumblings. It’s world history for the rest of us. ” - Yusuf al-Rahhal</p>
    </div>
    <div class="barcode-space"></div>
  </section>

  <section class="spine">
    <span class="spine-title">WANDERING PAST CHRONICLES</span>
    <span class="spine-author">Tobias Holloway</span>
  </section>

  <section class="front-cover">
    <svg class="shapes" viewBox="0 0 500 760" aria-hidden="true">
      <path d="M0 60 C60 40 160 30 260 40 C330 46 360 60 370 90 C380 120 350 150 330 190
               C310 230 330 260 340 300 C352 345 320 370 280 360 C240 350 230 320 200 320
               C170 320 160 350 150 390 C140 430 110 450 90 440 C70 430 80 380 85 330
               C90 270 60 240 30 220 C10 205 0 190 0 170 Z" fill="#2f2f2f"/>
    </svg>
    <p class="edition">Second Edition</p>
    <h1 class="title">
      <span class="line-1">Wandering</span>
      <span class="line-2">Past</span>
      <span class="line-3">Chronicles</span>
    </h1>
    <div class="globe" role="img" aria-label="Upside-down globe showing continents in dark grey"></div>
    <div class="globe-shadow"></div>
    <p class="subtitle">The Legends, Customs and Crossroads of Human Memory<br>and the Local Dilemmas of Our Age</p>
    <p class="author">Tobias Holloway</p>
  </section>

</main>
</body>
</html>
```